Biz card, letterhead, envelopes for massage business
Massage Business for people and for Equine (horses)
Biz card, letterhead, envelopes for massage business - Massage Therapy
Use same font as used in my logo
simular to my logo
Modern
Marla Kessin
Certified Massage Therapist
P.O. Box 871, Wrenhollow, ID 95718
marlakessin@quillpost.net
I provide massage for people and for horses. We need to creatively put the information on the back of the card. Of course we don't want to say "Human"..... when refering to horse we call it Equine Massage.
Human Massage Therapy.....Swedish, Deep Tissue, Relaxation, Hot Stone, On-Site Chair Massage Equine Massage Therapy...... Stridolan Certified Pellridge Method Relieves muscle pain, enhances performance, reduces inflamation, enhances muscle tone, increases endorphines - a horses natural pain killers For both : Relax Relieve Rejuvenate

```html
<!DOCTYPE html>
<html lang="en">
<head>
<meta charset="utf-8">
<title>Even Stride Wellness – Business Cards</title>
<link href="https://fonts.googleapis.com/css2?family=Open+Sans:wght@400;600&display=swap" rel="stylesheet">
<style>
  :root{
    --bg:#e9e4dd;
    --brown:#6b3a1f;
    --brown-dark:#4f2812;
    --brown-light:#8a5230;
    --green:#6f9a3c;
    --silver:#d9d9d9;
    --paper:#ffffff;
    --paper-shade:#e6e6e6;
    --ink-light:#f6ede5;
    --frost:rgba(255,255,255,.55);
    --frost-edge:rgba(255,255,255,.9);
  }
  *{box-sizing:border-box;margin:0;padding:0}
  html,body{width:1200px;height:730px;overflow:hidden}
  body{background:var(--bg);font-family:"Open Sans",Arial,sans-serif;position:relative}

  .card{position:absolute;width:463px;height:264px;border-radius:15px;overflow:hidden;
        box-shadow:0 4px 14px rgba(60,40,20,.25)}
  .card--front-solid{left:77px;top:60px}
  .card--front-clear{left:665px;top:60px}
  .card--back-solid{left:77px;top:405px}
  .card--back-clear{left:665px;top:405px}

  .card__top{position:absolute;left:0;top:0;width:100%;
             background:linear-gradient(180deg,var(--paper) 0%,var(--paper) 55%,var(--paper-shade) 100%)}
  .card--front-solid .card__top,.card--front-clear .card__top{height:150px}
  .card--back-solid .card__top,.card--back-clear .card__top{height:118px}
  .card--front-clear .card__top,.card--back-clear .card__top{
    background:linear-gradient(180deg,var(--frost-edge) 0%,var(--frost) 100%)}

  .card__band{position:absolute;left:0;bottom:0;width:100%;
              background:linear-gradient(180deg,var(--brown-light) 0%,var(--brown) 35%,var(--brown-dark) 100%);
              border-top:5px solid var(--silver)}
  .card--front-solid .card__band,.card--front-clear .card__band{top:145px}
  .card--back-solid .card__band,.card--back-clear .card__band{top:113px}
  .card--back-clear .card__band{opacity:.85}

  .brand{position:absolute;left:0;width:100%;display:flex;align-items:center;justify-content:center;gap:9px}
  .card--front-solid .brand,.card--front-clear .brand{top:70px}
  .card--back-solid .brand,.card--back-clear .brand{top:44px}
  .brand__dot{width:18px;height:18px;border:2px solid var(--green);border-radius:50%}
  .brand__name{font-weight:600;font-size:20px;color:var(--green);letter-spacing:.5px;text-transform:uppercase}

  .card--back-clear .card__mirror{position:absolute;inset:0;transform:scaleX(-1);opacity:.55}

  .identity{position:absolute;top:160px;left:0;width:100%;text-align:center;color:var(--ink-light);font-size:12.5px}
  .identity__divider{display:inline-block;width:1px;height:12px;background:var(--ink-light);margin:0 8px;vertical-align:-1px}
  .identity__role{font-size:10.5px}

  .contacts{position:absolute;top:200px;left:26px;right:20px;display:grid;
            grid-template-columns:1.15fr 1fr;row-gap:9px;column-gap:12px}
  .contact{display:flex;align-items:center;gap:7px;color:var(--ink-light);font-size:10px;white-space:nowrap}
  .contact__icon{width:14px;height:14px;flex:none}

  .web{position:absolute;top:185px;left:0;width:100%;text-align:center;color:var(--ink-light);
       font-size:12.5px;letter-spacing:2px}
</style>
</head>
<body>

<section class="card card--front-solid">
  <div class="card__top"></div>
  <div class="card__band"></div>
  <div class="brand"><span class="brand__dot"></span><span class="brand__name">Even Stride Wellness</span></div>
  <p class="identity">Marla Kessin<span class="identity__divider"></span><span class="identity__role">Certified Massage Therapist</span></p>
  <div class="contacts">
    <div class="contact">
      <svg class="contact__icon" viewBox="0 0 16 16"><circle cx="8" cy="8" r="8" fill="#f6ede5"/><path d="M8 3.5a2.8 2.8 0 0 0-2.8 2.8C5.2 8.6 8 12.5 8 12.5s2.8-3.9 2.8-6.2A2.8 2.8 0 0 0 8 3.5zm0 3.9a1.1 1.1 0 1 1 0-2.2 1.1 1.1 0 0 1 0 2.2z" fill="#6b3a1f"/></svg>
      P.O. Box 871, Wrenhollow, ID 95718</div>
    <div class="contact">
      <svg class="contact__icon" viewBox="0 0 16 16"><circle cx="8" cy="8" r="8" fill="#f6ede5"/><circle cx="8" cy="8" r="4.3" fill="none" stroke="#6b3a1f" stroke-width="1"/><ellipse cx="8" cy="8" rx="1.8" ry="4.3" fill="none" stroke="#6b3a1f" stroke-width="1"/><path d="M3.7 8h8.6" stroke="#6b3a1f" stroke-width="1"/></svg>
      www.evenstridecare.com</div>
    <div class="contact">
      <svg class="contact__icon" viewBox="0 0 16 16"><circle cx="8" cy="8" r="8" fill="#f6ede5"/><path d="M5.4 4.2l1.3-.3 1 2.2-.9.8a5.6 5.6 0 0 0 2.3 2.3l.8-.9 2.2 1-.3 1.3c-.1.4-.5.7-.9.7A6.6 6.6 0 0 1 4.7 5.1c0-.4.3-.8.7-.9z" fill="#6b3a1f"/></svg>
      208-555-0147</div>
    <div class="contact">
      <svg class="contact__icon" viewBox="0 0 16 16"><circle cx="8" cy="8" r="8" fill="#f6ede5"/><rect x="4" y="5.2" width="8" height="5.6" rx=".6" fill="none" stroke="#6b3a1f" stroke-width="1"/><path d="M4.2 5.5 8 8.5l3.8-3" fill="none" stroke="#6b3a1f" stroke-width="1"/></svg>
      marlakessin@quillpost.net</div>
  </div>
</section>

<section class="card card--front-clear">
  <div class="card__top"></div>
  <div class="card__band"></div>
  <div class="brand"><span class="brand__dot"></span><span class="brand__name">Even Stride Wellness</span></div>
  <p class="identity">Marla Kessin<span class="identity__divider"></span><span class="identity__role">Certified Massage Therapist</span></p>
  <div class="contacts">
    <div class="contact">
      <svg class="contact__icon" viewBox="0 0 16 16"><circle cx="8" cy="8" r="8" fill="#f6ede5"/><path d="M8 3.5a2.8 2.8 0 0 0-2.8 2.8C5.2 8.6 8 12.5 8 12.5s2.8-3.9 2.8-6.2A2.8 2.8 0 0 0 8 3.5zm0 3.9a1.1 1.1 0 1 1 0-2.2 1.1 1.1 0 0 1 0 2.2z" fill="#6b3a1f"/></svg>
      P.O. Box 871, Wrenhollow, ID 95718</div>
    <div class="contact">
      <svg class="contact__icon" viewBox="0 0 16 16"><circle cx="8" cy="8" r="8" fill="#f6ede5"/><circle cx="8" cy="8" r="4.3" fill="none" stroke="#6b3a1f" stroke-width="1"/><ellipse cx="8" cy="8" rx="1.8" ry="4.3" fill="none" stroke="#6b3a1f" stroke-width="1"/><path d="M3.7 8h8.6" stroke="#6b3a1f" stroke-width="1"/></svg>
      www.evenstridecare.com</div>
    <div class="contact">
      <svg class="contact__icon" viewBox="0 0 16 16"><circle cx="8" cy="8" r="8" fill="#f6ede5"/><path d="M5.4 4.2l1.3-.3 1 2.2-.9.8a5.6 5.6 0 0 0 2.3 2.3l.8-.9 2.2 1-.3 1.3c-.1.4-.5.7-.9.7A6.6 6.6 0 0 1 4.7 5.1c0-.4.3-.8.7-.9z" fill="#6b3a1f"/></svg>
      208-555-0147</div>
    <div class="contact">
      <svg class="contact__icon" viewBox="0 0 16 16"><circle cx="8" cy="8" r="8" fill="#f6ede5"/><rect x="4" y="5.2" width="8" height="5.6" rx=".6" fill="none" stroke="#6b3a1f" stroke-width="1"/><path d="M4.2 5.5 8 8.5l3.8-3" fill="none" stroke="#6b3a1f" stroke-width="1"/></svg>
      marlakessin@quillpost.net</div>
  </div>
</section>

<section class="card card--back-solid">
  <div class="card__top"></div>
  <div class="card__band"></div>
  <div class="brand"><span class="brand__dot"></span><span class="brand__name">Even Stride Wellness</span></div>
  <p class="web">www.evenstridecare.com</p>
</section>

<section class="card card--back-clear">
  <div class="card__top"></div>
  <div class="card__band"></div>
  <div class="card__mirror">
    <div class="brand"><span class="brand__dot"></span><span class="brand__name">Even Stride Wellness</span></div>
  </div>
  <p class="web">www.evenstridecare.com</p>
</section>

</body>
</html>
```